Lantern on The Hill Business Card Design

Simple 2 sided card ideally based around a zen garden approach (larger stone in a sand combed garden), but not essential.
Business is Project Management, IT Consultancy, Business Analysis.
Initially one person, however others may join the business so a unique logo would be preferred that encapsulates the approach of one pebble dropping in water causing many ripples. Potentially based around a zen garden, but not essential.
Clean and tidy, double sided, glossy, interesting and unique.
Company Name and contact details on one side (with the ability to replace the name, telephone and email address for more staff):
Lantern on The Hill Ltd
Dennis Hobart
077 5182 6271
dennis@lanternonthehill-example.com
Company name and offering on the other:
Lantern on The Hill Ltd
Project Management
Business Analysis
IT Consultancy
Interesting looking font, nice colours, not too many, but simple, effective and eye catching.
Potential Image either as a background or to the left/ right. Replicated on the rear of the card.
Design once approved and complete to be the sole property of Lantern on The Hill Ltd.
No requirement for Twitter, Facebook or Linked in details on any design
Lantern on The Hill
Dennis Hobart
077 5182 6271
Project Management
Business Analysis
IT Consultancy

```html
<!DOCTYPE html>
<html lang="en">
<head>
<meta charset="utf-8">
<title>Lantern on The Hill – Business Card</title>
<link rel="stylesheet" href="https://fonts.googleapis.com/css2?family=Open+Sans:wght@300;400;700&display=swap">
<style>
  :root {
    --backdrop: #e7e4de;
    --card-dark: #141414;
    --card-mid: #2b2b2a;
    --sand-light: #6d6b66;
    --stone: #3a3936;
    --title-ink: #d9d6c8;
    --body-ink: #a9a79f;
    --name-ink: #d2d0c6;
    --edge: #9b9a8a;
  }
  * { margin: 0; padding: 0; box-sizing: border-box; }
  html, body {
    width: 1200px;
    height: 913px;
    overflow: hidden;
    background: var(--backdrop);
  }
  .sheet {
    position: relative;
    width: 1200px;
    height: 913px;
    display: flex;
    align-items: center;
    justify-content: center;
    gap: 40px;
  }
  .card {
    position: relative;
    width: 540px;
    height: 309px;
    overflow: hidden;
    border-radius: 3px;
    background: var(--card-dark);
    box-shadow: 0 0 0 1px var(--edge), 0 14px 30px rgba(0,0,0,0.25);
  }
  .card-image {
    position: absolute;
    inset: 0;
    background:
      radial-gradient(ellipse 22% 24% at 26% 30%, var(--stone) 0%, rgba(58,57,54,0) 100%),
      radial-gradient(ellipse 26% 26% at 30% 62%, #323130 0%, rgba(50,49,48,0) 100%),
      radial-gradient(ellipse 55% 70% at 80% 20%, var(--sand-light) 0%, rgba(109,107,102,0) 100%),
      linear-gradient(160deg, var(--card-mid) 0%, var(--card-dark) 70%);
  }
  .gloss {
    position: absolute;
    inset: 0;
    background: linear-gradient(115deg, rgba(255,255,255,0) 40%, rgba(255,255,255,0.07) 48%, rgba(255,255,255,0) 56%);
  }
  .company-name {
    position: absolute;
    font-family: "Open Sans", Arial, sans-serif;
    font-weight: 300;
    color: var(--title-ink);
    letter-spacing: 0;
    white-space: nowrap;
  }
  .front .company-name {
    left: 46px;
    top: 148px;
    font-size: 36px;
    line-height: 1.2;
  }
  .offering {
    position: absolute;
    left: 47px;
    top: 212px;
    font-family: "Open Sans", Arial, sans-serif;
    font-weight: 300;
    font-size: 14px;
    color: var(--body-ink);
    letter-spacing: 0.02em;
    white-space: nowrap;
  }
  .offering .divider { margin: 0 8px; }
  .back .company-name {
    left: 34px;
    top: 226px;
    font-size: 24px;
    line-height: 1.2;
  }
  .contact {
    position: absolute;
    left: 250px;
    top: 62px;
    font-family: "Open Sans", Arial, sans-serif;
    color: var(--body-ink);
    white-space: nowrap;
  }
  .person-name {
    font-weight: 700;
    font-size: 17px;
    color: var(--name-ink);
    line-height: 1.2;
  }
  .person-role {
    font-weight: 400;
    font-size: 13px;
    line-height: 1.3;
  }
  .contact-list {
    list-style: none;
    margin-top: 26px;
    margin-left: 8px;
    font-size: 12.5px;
    line-height: 1.55;
  }
  .contact-list li { display: flex; align-items: center; gap: 8px; }
  .contact-icon { width: 12px; height: 12px; fill: var(--body-ink); flex: none; }
</style>
</head>
<body>
  <main class="sheet">
    <section class="card front" aria-label="Card front">
      <div class="card-image" role="img" aria-label="Stacked pebbles resting in raked zen garden sand, dark toned"></div>
      <div class="gloss"></div>
      <h1 class="company-name">Lantern on The Hill</h1>
      <p class="offering">Project Management<span class="divider">|</span>Business Analysis<span class="divider">|</span>IT Consultancy</p>
    </section>

    <section class="card back" aria-label="Card back">
      <div class="card-image" role="img" aria-label="Stacked pebbles resting in raked zen garden sand, dark toned"></div>
      <div class="gloss"></div>
      <h2 class="company-name">Lantern on The Hill</h2>
      <div class="contact">
        <p class="person-name">Dennis Hobart</p>
        <p class="person-role">Managing Director</p>
        <ul class="contact-list">
          <li>
            <svg class="contact-icon" viewBox="0 0 12 12" aria-hidden="true"><path d="M1 3.5C1 2 2.5 1.5 6 1.5S11 2 11 3.5V5H8.5V4H3.5V5H1z M2.5 6h7l1 4.5h-9z"/></svg>
            <span>077 5182 6271</span>
          </li>
          <li>
            <svg class="contact-icon" viewBox="0 0 12 12" aria-hidden="true"><path d="M1 2.5h10v7H1z M1.6 3.1 6 6.6l4.4-3.5" stroke="#2b2b2a" stroke-width="0.8"/></svg>
            <span>dennis@lanternonthehill-example.com</span>
          </li>
        </ul>
      </div>
    </section>
  </main>
</body>
</html>
```